AUSTRALIAN CONSULTING FIRM BUSINESS CARD - MODERN

We are wanting a modern, clean lined business card design. We are professional niche consultancy firm situated in Australia called Marlow Advisory Partners Pty Ltd.
The card should communicate professionalism and creativity and draw on our logo design (attached).
The design should be two sided, landscape orientation.
Target Market(s)
government, not for profit sector, corporate clients
Industry/Entity Type
Landscape
Requirements
Must have
- logo
no new introduced colours

```html
<!DOCTYPE html>
<html lang="en">
<head>
<meta charset="utf-8">
<title>Marlow Advisory Partners – Business Card</title>
<link href="https://fonts.googleapis.com/css2?family=Arimo:wght@400;700&family=Roboto+Condensed:wght@300;400&display=swap" rel="stylesheet">
<style>
  :root {
    --page-bg: #ffffff;
    --card-front: #ffffff;
    --card-edge: #d9d9d9;
    --swoosh: #eeeeee;
    --card-back: #0094dc;
    --navy: #23317f;
    --name-dark: #1c2a4a;
    --white: #ffffff;
  }
  * { margin: 0; padding: 0; box-sizing: border-box; }
  html, body {
    width: 1166px;
    height: 1200px;
    overflow: hidden;
    background: var(--page-bg);
  }
  .canvas {
    position: relative;
    width: 1166px;
    height: 1200px;
  }
  .card {
    position: absolute;
    left: 208px;
    width: 747px;
    height: 400px;
    overflow: hidden;
  }
  .card--front {
    top: 188px;
    background: var(--card-front);
    border: 1px solid var(--card-edge);
    border-radius: 130px 14px 14px 14px;
  }
  .card--back {
    top: 618px;
    background: var(--card-back);
    border-radius: 14px 14px 14px 130px;
  }
  .swoosh {
    position: absolute;
    inset: 0;
    width: 100%;
    height: 100%;
  }
  .brand {
    position: absolute;
    left: 196px;
    top: 138px;
    display: flex;
    align-items: center;
    gap: 22px;
  }
  .brand__dot {
    width: 42px;
    height: 42px;
    border-radius: 50%;
    background: var(--navy);
    flex: none;
  }
  .brand__name {
    font-family: "Arimo", Arial, sans-serif;
    font-weight: 700;
    font-size: 38px;
    line-height: 1.12;
    letter-spacing: 0.5px;
    color: var(--navy);
  }
  .contact {
    position: absolute;
    left: 0;
    right: 0;
    top: 145px;
    text-align: center;
    color: var(--white);
  }
  .contact__company {
    font-family: "Roboto Condensed", "Arial Narrow", sans-serif;
    font-weight: 400;
    font-size: 27px;
    margin-bottom: 20px;
  }
  .contact__company-tail { color: var(--name-dark); }
  .contact__line {
    font-family: "Arimo", Arial, sans-serif;
    font-size: 20px;
    line-height: 30px;
  }
</style>
</head>
<body>
  <main class="canvas">
    <section class="card card--front" aria-label="Card front">
      <svg class="swoosh" viewBox="0 0 747 400" preserveAspectRatio="none" aria-hidden="true">
        <path d="M0,345 Q120,70 316,0 L700,0 Q330,60 94,400 L0,400 Z" fill="var(--swoosh)"/>
      </svg>
      <div class="brand">
        <span class="brand__dot"></span>
        <p class="brand__name">MARLOW ADVISORY<br>PARTNERS PTY LTD</p>
      </div>
    </section>

    <section class="card card--back" aria-label="Card back">
      <div class="contact">
        <p class="contact__company">Marlow Advisory <span class="contact__company-tail">Partners Pty Ltd.</span></p>
        <p class="contact__line">Tel :111-222-0000</p>
        <p class="contact__line">E-mail : 123@companyname.com</p>
        <p class="contact__line">Web : www.companyname.com</p>
      </div>
    </section>
  </main>
</body>
</html>
```